Small Business Consulting Firm Needs Business Card Design

Need a sleek modern business card with 2 sides matching the colors of our logo. We will be placing these with a mailer we are sending out. These business cards will only ever be given to business owners. We operate helping businesses who are struggling with cash flow or finances. If the green and blue design needs to be moved to the right of "Harborline Crest Consulting" for aesthetic purposes that is ok. We will need an editable file if possible. We would like to include the reps name, email, website, and phone number. For now just use Peter Vance, pvance@harborlinecrest.com, www.harborlinecrest.com, and 833-555-0172.

```html
<!DOCTYPE html>
<html lang="en">
<head>
<meta charset="utf-8">
<title>Harborline Crest Consulting – Business Card</title>
<link href="https://fonts.googleapis.com/css2?family=Open+Sans:wght@300;400;700&display=swap" rel="stylesheet">
<style>
  :root {
    --bg: #2a2b2d;
    --card-white: #ffffff;
    --green: #6aaa3c;
    --green-light: #74b640;
    --green-dark: #5e9a35;
    --blue: #1f66b0;
    --ink: #3d3d3d;
    --grey-rule: #9a9a9a;
  }
  * { box-sizing: border-box; margin: 0; padding: 0; }
  html, body { width: 1200px; height: 960px; overflow: hidden; }
  body {
    background: var(--bg);
    font-family: "Open Sans", Arial, sans-serif;
    position: relative;
  }
  .card {
    position: absolute;
    left: 290px;
    width: 620px;
    height: 354px;
    overflow: hidden;
    box-shadow: 0 12px 28px rgba(0,0,0,.45);
  }
  /* Back side */
  .card-back {
    top: 70px;
    background: linear-gradient(160deg, var(--green-light), var(--green-dark));
  }
  .card-back .brand {
    position: absolute;
    top: 140px; left: 0; right: 0;
    display: flex; justify-content: center; align-items: center; gap: 14px;
  }
  .card-back .brand-square {
    width: 30px; height: 30px; background: #ffffff;
  }
  .card-back .brand-name {
    color: #ffffff; font-weight: 300; font-size: 26px; letter-spacing: 3px; text-transform: uppercase;
  }
  .card-back .back-url {
    position: absolute; bottom: 34px; left: 0; right: 0;
    text-align: center; color: #ffffff; font-size: 15px; letter-spacing: 6px;
  }
  /* Front side */
  .card-front {
    top: 500px;
    background: var(--card-white);
  }
  .front-logo {
    position: absolute; left: 40px; top: 120px; width: 250px;
    display: flex; flex-direction: column; align-items: center; gap: 8px;
  }
  .front-logo .brand-square { width: 34px; height: 34px; background: var(--green); }
  .front-logo .brand-name {
    color: var(--ink); font-weight: 300; font-size: 19px; letter-spacing: 2px;
    text-transform: uppercase; text-align: center; line-height: 1.3;
  }
  .divider {
    position: absolute; left: 318px; top: 90px; width: 1px; height: 150px;
    background: linear-gradient(to bottom, transparent, var(--grey-rule) 30%, var(--grey-rule) 70%, transparent);
  }
  .contact {
    position: absolute; left: 345px; top: 102px;
  }
  .rep-name {
    color: var(--green); font-weight: 700; font-size: 27px; margin-bottom: 10px;
  }
  .contact-list { list-style: none; }
  .contact-list li {
    display: flex; align-items: center; gap: 9px;
    color: var(--ink); font-size: 17px; line-height: 27px;
  }
  .contact-list svg { width: 15px; height: 15px; flex: none; fill: var(--green); }
  .band-blue {
    position: absolute; left: 0; right: 0; bottom: 18px; height: 4px; background: var(--blue);
  }
  .band-green {
    position: absolute; left: 0; right: 0; bottom: 0; height: 16px; background: var(--green);
  }
</style>
</head>
<body>
  <section class="card card-back">
    <div class="brand">
      <span class="brand-square"></span>
      <span class="brand-name">Harborline Crest</span>
    </div>
    <p class="back-url">www.harborlinecrest.com</p>
  </section>

  <section class="card card-front">
    <div class="front-logo">
      <span class="brand-square"></span>
      <span class="brand-name">Harborline Crest Consulting</span>
    </div>
    <div class="divider"></div>
    <div class="contact">
      <h1 class="rep-name">Peter Vance</h1>
      <ul class="contact-list">
        <li>
          <svg viewBox="0 0 16 16" aria-hidden="true"><path d="M3.5 1l2.5 3-1.5 1.8a9 9 0 0 0 5.7 5.7L12 10l3 2.5-1.6 2.3C7.5 15 1 8.5 1.2 2.6z"/></svg>
          833-555-0172
        </li>
        <li>
          <svg viewBox="0 0 16 16" aria-hidden="true"><path d="M1 3h14v10H1z M1.5 3.5L8 9l6.5-5.5" fill="none" stroke="#6aaa3c" stroke-width="1.6"/></svg>
          pvance@harborlinecrest.com
        </li>
        <li>
          <svg viewBox="0 0 16 16" aria-hidden="true"><circle cx="8" cy="8" r="6.5" fill="none" stroke="#6aaa3c" stroke-width="1.5"/><path d="M1.5 8h13M8 1.5c-3 3.5-3 9.5 0 13M8 1.5c3 3.5 3 9.5 0 13" fill="none" stroke="#6aaa3c" stroke-width="1.2"/></svg>
          www.harborlinecrest.com
        </li>
      </ul>
    </div>
    <div class="band-blue"></div>
    <div class="band-green"></div>
  </section>
</body>
</html>
```